One-Page Flat Design for SEO Company [2 DAYS]

We need a one-page flat design for our SEO company. Our current website is http://www.rankorchard.com/. We are looking to completely re-design the site using new flat design techniques.
Below are some examples of the type of style we're going after:
http://pelmora.com/
http://tobyharlan.co.uk/
https://quillet.co/
http://marcusfenley.me/
As you can see- flat, clean, minimal. It is very important you follow this type of style.
For colour scheme, you may use one of the pre-made colour palettes from here:
http://www.wavecrestlab.com/blog/inspiration/24-flat-designs-with-compelling-color-palettes
I've attached a wireframe to be followed.
Hi,

```html
<!DOCTYPE html>
<html lang="en">
<head>
<meta charset="utf-8">
<title>RankOrchard – SEO Services</title>
<link href="https://fonts.googleapis.com/css2?family=Open+Sans:wght@300;400;600;700&display=swap" rel="stylesheet">
<style>
:root{
  --orange:#f5a00f;
  --orange-dark:#e58e00;
  --cell:#fde7b5;
  --cell-alt:#fbd98c;
  --ink:#444;
  --muted:#777;
  --line:#e4e4e4;
  --panel:#f1f1f1;
  --footer:#2b3036;
  --white:#fff;
}
*{box-sizing:border-box;margin:0;padding:0}
html,body{width:1200px;height:3628px;overflow:hidden}
body{font-family:'Open Sans',Arial,sans-serif;color:var(--ink);background:var(--white);position:relative}
.abs{position:absolute}

/* header + hero */
.hero{left:0;top:0;width:1200px;height:700px;
  background:radial-gradient(circle at 78% 20%,#d8d2cc 0,#f3f0ee 30%,transparent 55%),
             radial-gradient(circle at 20% 35%,#e6e2df 0,#fbfaf9 40%),#f7f6f5}
.hero-dice{left:620px;top:0;width:560px;height:560px;
  background:radial-gradient(circle at 50% 45%,#f4f1ef 0,#e3dcd8 45%,rgba(220,60,60,.15) 70%,transparent 72%)}
.logo{left:28px;top:12px;display:flex;align-items:center;gap:10px}
.logo-mark{width:30px;height:30px;background:var(--orange);border-radius:50%}
.logo-name{font-weight:700;font-size:28px;color:var(--orange);letter-spacing:-.5px}
.nav{right:40px;top:26px;display:flex;gap:34px;font-size:13px;font-weight:600;color:var(--orange);text-transform:uppercase}
.hero-title{left:0;width:1200px;top:196px;text-align:center;font-size:27px;font-weight:700;color:#333;letter-spacing:.5px}
.hero-text{left:160px;width:880px;top:385px;text-align:center;font-size:30px;font-weight:300;line-height:46px;color:#555;text-transform:uppercase}
.hero-down{left:570px;top:620px;width:60px;height:60px;border:2px solid #fff;border-radius:50%;background:rgba(0,0,0,.12)}
.hero-down-label{left:500px;width:200px;top:688px;text-align:center;font-size:10px;color:#888;letter-spacing:1px}

/* section headings */
.sec-title{left:0;width:1200px;text-align:center;font-size:48px;font-weight:300;color:#333;letter-spacing:1px}
.sec-rule{left:560px;width:80px;height:4px;background:var(--orange)}
.sec-sub{left:200px;width:800px;text-align:center;font-size:17px;line-height:26px;color:var(--muted);text-transform:uppercase}

/* about features */
.features{left:0;top:1030px;width:1200px;height:260px;background:#fafafa;border-top:1px solid var(--line);border-bottom:1px solid var(--line)}
.feature{top:1070px;width:260px;height:170px;background:var(--panel);border:1px solid var(--line);text-align:center;padding-top:22px}
.feature-icon{width:46px;height:46px;margin:0 auto 22px;border-radius:50%;background:var(--orange)}
.feature p{font-size:14px;line-height:20px;color:#555;padding:0 26px}

.to-top{left:1130px;width:44px;height:44px;border-radius:50%;background:#777}

/* pricing table */
.plan-label{left:0;width:1200px;top:1512px;text-align:center;font-size:19px;color:#555}
.plan-rule{left:440px;top:1500px;width:320px;height:1px;background:var(--line)}
.pricing{left:88px;top:1585px;width:1012px;border-collapse:collapse;font-size:11px}
.pricing th,.pricing td{border:1px solid #fff;height:38px;text-align:center}
.pricing thead th{background:var(--orange);color:#fff;font-weight:600;height:44px;font-size:12px}
.pricing tbody th{background:var(--orange);color:#fff;font-weight:700;text-align:left;padding-left:12px;width:272px}
.pricing tbody td{background:var(--cell);color:#333}
.pricing tbody tr:nth-child(even) td{background:var(--cell-alt)}
.pricing .price th{height:64px;font-size:12px}
.pricing .price td{font-size:34px;color:var(--orange-dark);font-weight:600;background:var(--cell)}

/* contact */
.form-head{left:170px;top:2355px;font-size:17px;color:#555}
.form-row{left:100px;width:480px;display:flex;align-items:flex-start}
.form-row label{width:70px;font-size:13px;text-align:right;padding-right:10px;padding-top:6px}
.form-row .field{flex:1;height:30px;border:1px solid #ccc;background:#fff}
.form-row .field.area{height:140px}
.send{left:180px;top:2775px;width:100px;height:34px;background:var(--orange);color:#fff;font-size:13px;text-align:center;line-height:34px}
.info-head{left:704px;top:2346px;font-size:19px;color:#444}
.info-line{left:706px;font-size:13px;color:#555;display:flex;align-items:center;gap:10px}
.info-line svg{flex:none}
.office-head{left:704px;top:2500px;font-size:19px;color:var(--orange-dark)}
.office-photo{left:704px;top:2532px;width:456px;height:170px;background:linear-gradient(135deg,#cfd6dd,#8f9aa3 60%,#5d6a75)}

.map{left:0;top:2856px;width:1200px;height:336px;background:linear-gradient(160deg,#e9e5dc 0,#dcd6c9 40%,#b9d3e6 62%,#a9c8df)}

/* footer */
.footer{left:0;top:3192px;width:1200px;height:436px;background:var(--footer)}
.foot-logo{left:0;width:1200px;top:3245px;display:flex;justify-content:center;align-items:center;gap:8px}
.foot-logo .logo-mark{width:22px;height:22px}
.foot-logo .logo-name{font-size:22px}
.socials{left:0;width:1200px;top:3315px;display:flex;justify-content:center;gap:14px}
.socials span{width:30px;height:30px;border-radius:50%;border:2px solid #cfd3d8}
.foot-nav{left:0;width:1200px;top:3378px;display:flex;justify-content:center;gap:34px;font-size:15px;color:#e5e5e5}
.copyright{left:0;width:1200px;top:3418px;text-align:center;font-size:12px;color:#aab}
</style>
</head>
<body>

<div class="abs hero" role="img" aria-label="Hero photograph of two large white dice with red pips"></div>
<div class="abs hero-dice" role="img" aria-label="Close-up of tumbling dice"></div>
<div class="abs logo"><span class="logo-mark"></span><span class="logo-name">RankOrchard</span></div>
<nav class="abs nav"><span>Home</span><span>About</span><span>Services</span><span>Blog</span><span>Contact</span></nav>
<h1 class="abs hero-title">BOOST YOUR RANKINGS WITH OUR GUARANTEED SEO SERVICES</h1>
<p class="abs hero-text">We provide high-quality SEO services that are guaranteed to give your rankings a boost. As of 2013, all of our services are 100% Searchly friendly and are compatible with latest Pinefall and Larkspur updates.</p>
<div class="abs hero-down"><svg width="56" height="56" viewBox="0 0 56 56"><path d="M18 24l10 10 10-10" fill="none" stroke="#fff" stroke-width="3"/></svg></div>
<div class="abs hero-down-label">SCROLL DOWN</div>

<h2 class="abs sec-title" style="top:722px">ABOUT US</h2>
<div class="abs sec-rule" style="top:795px"></div>
<p class="abs sec-sub" style="top:830px">Why spend countless hours trying to increase your search engine rankings? At RankOrchard.com, we know how important backlinks are to your website.</p>

<div class="abs features"></div>
<div class="abs feature" style="left:40px"><div class="feature-icon"><svg width="46" height="46" viewBox="0 0 46 46"><path d="M14 30h18M16 30V18h14v12M23 12v6" fill="none" stroke="#fff" stroke-width="3"/></svg></div><p>Professional Backlink SEO Services</p></div>
<div class="abs feature" style="left:330px"><div class="feature-icon"><svg width="46" height="46" viewBox="0 0 46 46"><text x="23" y="31" text-anchor="middle" font-size="22" font-weight="700" fill="#fff" font-family="Open Sans,sans-serif">$</text></svg></div><p>We Provide Real Backlink In Affordable Prices</p></div>
<div class="abs feature" style="left:620px"><div class="feature-icon"><svg width="46" height="46" viewBox="0 0 46 46"><rect x="14" y="21" width="18" height="13" fill="#fff"/><path d="M17 21v-4a6 6 0 0 1 12 0v4" fill="none" stroke="#fff" stroke-width="3"/></svg></div><p>Safe And Risk Free Methods Of Backlinking</p></div>
<div class="abs feature" style="left:910px"><div class="feature-icon"><svg width="46" height="46" viewBox="0 0 46 46"><path d="M14 24l6 6 12-13" fill="none" stroke="#fff" stroke-width="4"/></svg></div><p>Manual Services With Quality Without Black hat techniques</p></div>
<div class="abs to-top" style="top:1212px"><svg width="44" height="44" viewBox="0 0 44 44"><path d="M15 25l7-7 7 7" fill="none" stroke="#fff" stroke-width="3"/></svg></div>

<h2 class="abs sec-title" style="top:1358px">OUR SERVICES</h2>
<div class="abs sec-rule" style="top:1430px"></div>
<p class="abs sec-sub" style="top:1446px">At RankOrchard.com, we offer a variety of SEO services.</p>
<div class="abs plan-rule"></div>
<div class="abs plan-label">OUR PLAN</div>

<table class="abs pricing">
<thead><tr><th></th><th>Bronze Package</th><th>Silver Package</th><th>Gold Package</th><th>Platinum Package</th></tr></thead>
<tbody>
<tr><th>Full SEO Audit</th><td>-</td><td>-</td><td>-</td><td><svg width="22" height="18" viewBox="0 0 22 18"><path d="M2 9l6 6L20 2" fill="none" stroke="#6fb33a" stroke-width="4"/></svg></td></tr>
<tr><th>LinkWheels</th><td>-</td><td>-</td><td>5 PR3 - PR7</td><td>5 PR3 - PR7</td></tr>
<tr><th>Social Bookmarks</th><td>10 PR3 - PR8</td><td>10 PR3 - PR8</td><td>10 PR3 - PR8</td><td>10 PR3 - PR8</td></tr>
<tr><th>Web 2.0 Profile Backlinks</th><td>15 PR3 - PR8</td><td>15 PR3 - PR8</td><td>15 PR3 - PR8</td><td>45 PR3 - PR8</td></tr>
<tr><th>EDU Backlinks</th><td>100</td><td>100</td><td>100</td><td>100</td></tr>
<tr><th>Backlinks</th><td>150 PR3 - PR7</td><td>150 PR3 - PR7</td><td>150 PR3 - PR7</td><td>150 PR3 - PR7</td></tr>
<tr><th>Profile Backlinks</th><td>-</td><td>2000</td><td>4000</td><td>6000</td></tr>
<tr><th>Blog Comments</th><td>-</td><td>4000</td><td>6000</td><td>12000</td></tr>
<tr><th>Wiki Backlinks</th><td>-</td><td>-</td><td>-</td><td>1500</td></tr>
<tr><th>Articles</th><td>-</td><td>-</td><td>-</td><td>300</td></tr>
<tr class="price"><th>Price per month</th><td>$ 39.00</td><td>$ 58.00</td><td>$ 79.00</td><td>$ 139.00</td></tr>
</tbody>
</table>
<div class="abs to-top" style="top:1846px"><svg width="44" height="44" viewBox="0 0 44 44"><path d="M15 25l7-7 7 7" fill="none" stroke="#fff" stroke-width="3"/></svg></div>

<h2 class="abs sec-title" style="top:2200px">CONTACT US</h2>
<div class="abs sec-rule" style="top:2272px"></div>
<p class="abs sec-sub" style="top:2290px">We are looking forward to hear from you</p>

<div class="abs form-head">Send us a message</div>
<div class="abs form-row" style="top:2380px"><label>Name<sup>*</sup></label><span class="field"></span></div>
<div class="abs form-row" style="top:2428px"><label>Email<sup>*</sup></label><span class="field"></span></div>
<div class="abs form-row" style="top:2476px"><label>Title</label><span class="field"></span></div>
<div class="abs form-row" style="top:2524px"><label>Message<sup>*</sup></label><span class="field area"></span></div>
<div class="abs send">SEND</div>

<div class="abs info-head">Contact info</div>
<div class="abs info-line" style="top:2388px"><svg width="12" height="16" viewBox="0 0 12 16"><path d="M6 0a6 6 0 0 1 6 6c0 4-6 10-6 10S0 10 0 6a6 6 0 0 1 6-6z" fill="var(--orange)"/><circle cx="6" cy="6" r="2" fill="#fff"/></svg>Address: 1234 Street Name City Name United States</div>
<div class="abs info-line" style="top:2420px"><svg width="12" height="16" viewBox="0 0 12 16"><rect x="1" y="0" width="10" height="16" rx="2" fill="var(--orange)"/><rect x="3" y="2" width="6" height="9" fill="#fff"/></svg>Phone: 123-456-7890</div>
<div class="abs info-line" style="top:2452px"><svg width="14" height="10" viewBox="0 0 14 10"><rect width="14" height="10" fill="var(--orange)"/><path d="M0 0l7 6 7-6" fill="none" stroke="#fff" stroke-width="1.5"/></svg>Email: <span style="color:var(--orange-dark)">mail@example.com</span></div>
<div class="abs office-head">OUR OFFICE</div>
<div class="abs office-photo" role="img" aria-label="Photograph of the open-plan office interior"></div>
<div class="abs to-top" style="top:2620px"><svg width="44" height="44" viewBox="0 0 44 44"><path d="M15 25l7-7 7 7" fill="none" stroke="#fff" stroke-width="3"/></svg></div>

<div class="abs map" role="img" aria-label="Street map of the city and coastline around the office location"></div>

<footer class="abs footer"></footer>
<div class="abs foot-logo"><span class="logo-mark"></span><span class="logo-name">RankOrchard</span></div>
<div class="abs socials"><span></span><span></span><span></span><span></span></div>
<nav class="abs foot-nav"><span>Home</span><span>About</span><span>Services</span><span>Blog</span><span>Contact</span></nav>
<p class="abs copyright">Copyright © 2014 RankOrchard . All rights reserved.</p>

</body>
</html>
```